Podcast Cover Design - Headline At Quiet Tables

We renamed our podcast from the "Harborline Property Podcast" to "Headlines At Quiet Tables" and we need a new podcast cover design, Instagram profile picture, and a YouTube banner.

More so we're looking for some sort of symbol/icon. Our old logo had the Copper Lantern but we're moving to a much broader audience that isn't necessarily from Seattle and needs something that will appeal to them.

In the podcast, Dale reads the news that big media isn't covering including crime, business, homeless crisis, protests. We stay away from covering politics but our audience is mainly right-wing.

Attached are some additional designs we created in-house.

If we love the design we'll have additional job opportunities to create possible designs for merchandise.

Target Market(s)

80% Males aged 50+, Republican

Industry/Entity Type

News

Colors

Designer to choose colors to be used in the design.

Requirements
Must have
• OPEN TOO IDEAS
Nice to have
• OPEN TOO IDEAS
Should not have
• Copper Lantern

```html
<!DOCTYPE html>
<html lang="en">
<head>
<meta charset="utf-8">
<title>Headlines At Quiet Tables – Podcast Cover</title>
<link href="https://fonts.googleapis.com/css2?family=Anton&family=Montserrat:wght@300;400;700&display=swap" rel="stylesheet">
<style>
  :root{
    --navy:#075a7e;
    --red:#de3636;
    --white:#ffffff;
    --photo:#9a6470;
  }
  html,body{margin:0;padding:0;overflow:hidden;background:var(--navy);}
  .cover{position:relative;width:1200px;height:1200px;background:var(--navy);overflow:hidden;font-family:'Montserrat',sans-serif;color:var(--white);}
  .banner{position:absolute;left:0;top:0;}
  .title-top{position:absolute;left:0;top:22px;width:1200px;text-align:center;font-family:'Anton',sans-serif;font-size:200px;line-height:1;letter-spacing:4px;padding-left:10px;box-sizing:border-box;}
  .title-mid{position:absolute;left:0;top:356px;width:1200px;text-align:center;font-weight:700;font-size:82px;line-height:1;letter-spacing:2px;padding-right:40px;box-sizing:border-box;}
  .title-bottom{position:absolute;left:0;top:432px;width:1200px;text-align:center;font-family:'Anton',sans-serif;font-size:330px;line-height:1;letter-spacing:6px;padding-right:20px;box-sizing:border-box;}
  .host-stage{position:absolute;left:0;top:0;}
  .host-photo{position:absolute;left:670px;top:706px;width:430px;height:494px;border-radius:24px 24px 0 0;background:var(--photo);}
  .mic-icon{position:absolute;left:127px;top:789px;}
  .host-label{position:absolute;left:127px;top:946px;font-weight:300;font-size:50px;line-height:1;letter-spacing:1px;}
  .host-name{position:absolute;left:127px;top:1014px;font-weight:700;font-size:62px;line-height:1.2;letter-spacing:1px;}
</style>
</head>
<body>
<div class="cover">
  <svg class="banner" width="1200" height="1200" viewBox="0 0 1200 1200">
    <polygon points="65,0 1124,0 952,336 198,336" fill="var(--red)"/>
  </svg>

  <div class="title-top">HEADLINES</div>
  <div class="title-mid">AT QUIET</div>
  <div class="title-bottom">TABLES</div>

  <svg class="host-stage" width="1200" height="1200" viewBox="0 0 1200 1200">
    <circle cx="922" cy="1306" r="450" fill="var(--red)" stroke="var(--white)" stroke-width="4"/>
  </svg>
  <div class="host-photo" role="img" aria-label="Portrait photo of host Dale Marlow beside a vintage studio microphone"></div>

  <svg class="mic-icon" width="140" height="142" viewBox="0 0 140 142" fill="none" stroke="var(--white)" stroke-linecap="round" stroke-width="9">
    <rect x="48" y="6" width="44" height="76" rx="22" fill="var(--white)" stroke="none"/>
    <path d="M40 70 v4 a30 30 0 0 0 60 0 v-4"/>
    <line x1="70" y1="104" x2="70" y2="132"/>
    <line x1="48" y1="134" x2="92" y2="134"/>
    <path d="M30 24 a50 50 0 0 0 0 56"/>
    <path d="M110 24 a50 50 0 0 1 0 56"/>
    <path d="M14 6 a80 80 0 0 0 0 92"/>
    <path d="M126 6 a80 80 0 0 1 0 92"/>
  </svg>

  <div class="host-label">WITH HOST</div>
  <div class="host-name">DALE<br>MARLOW</div>
</div>
</body>
</html>
```